Korvanta Business Card

Looking for business card ideas. Company name is Korvanta. Have a few basic ideas on attachment. Please submit anything with the logo and general information from attachment.

Industry/Entity Type

Business

```html
<!DOCTYPE html>
<html lang="en">
<head>
<meta charset="utf-8">
<title>Korvanta Business Card</title>
<link rel="stylesheet" href="https://fonts.googleapis.com/css2?family=Questrial&display=swap">
<style>
  :root {
    --backdrop: #1b1b1c;
    --card: #6d6e70;
    --brand-red: #d3241f;
    --accent-orange: #f0961c;
    --ink-dark: #151515;
    --ink-light: #ffffff;
  }
  * { margin: 0; padding: 0; box-sizing: border-box; }
  html, body {
    width: 1200px; height: 758px; overflow: hidden;
    background: var(--backdrop);
    font-family: "Questrial", "Century Gothic", sans-serif;
  }
  .business-card {
    position: absolute; left: 75px; top: 79px;
    width: 1050px; height: 600px;
    background: var(--card);
    overflow: hidden;
  }
  .card-graphics { position: absolute; inset: 0; }
  .tagline {
    position: absolute; right: 150px; top: 28px;
    color: var(--brand-red); font-size: 24px; letter-spacing: 0.5px;
    white-space: nowrap;
  }
  .brand {
    position: absolute; left: 50px; top: 92px;
    display: flex; align-items: center; gap: 22px;
  }
  .brand-dot {
    width: 104px; height: 104px; border-radius: 50%;
    background: var(--brand-red);
  }
  .brand-name {
    color: var(--brand-red); font-size: 76px; letter-spacing: 6px; line-height: 1;
  }
  .person-name {
    position: absolute; left: 600px; top: 218px;
    color: var(--ink-light); font-size: 34px;
  }
  .contact-list, .address-block {
    position: absolute; list-style: none;
    color: var(--ink-dark); font-size: 29px; line-height: 44px;
  }
  .contact-list { left: 60px; top: 352px; }
  .contact-list .label { display: inline-block; margin-left: 26px; }
  .address-block { right: 48px; top: 322px; text-align: right; line-height: 40px; }
</style>
</head>
<body>
  <article class="business-card">
    <svg class="card-graphics" viewBox="0 0 1050 600" width="1050" height="600" aria-hidden="true">
      <rect class="top-band" x="285" y="0" width="765" height="24" fill="var(--brand-red)"/>
      <rect class="bottom-band" x="0" y="530" width="370" height="34" fill="var(--accent-orange)"/>
      <polyline class="pulse-line" fill="none" stroke="var(--accent-orange)" stroke-width="6"
        points="0,508 500,508 540,320 598,575 640,575 640,545 1050,545"/>
    </svg>

    <p class="tagline">Guiding Groups to a Brighter Day</p>

    <div class="brand">
      <span class="brand-dot"></span>
      <span class="brand-name">Korvanta</span>
    </div>

    <p class="person-name">Marlo Dentry, Dir.</p>

    <ul class="contact-list">
      <li>(555) 310-4827<span class="label">Office</span></li>
      <li>(555) 310-9264<span class="label">Cell</span></li>
      <li>mdentry@korvanta.org</li>
    </ul>

    <ul class="address-block">
      <li>2740 W. Larkspur Ave.</li>
      <li>Brenford, TX 70123</li>
      <li>www.korvanta.org</li>
    </ul>
  </article>
</body>
</html>
```